Global Expert Network Firm needs business card design

We need business card design for a new company based in Seoul, South Korea called 'Corwell Insight Partners'. We recruit industry experts covering all countries and connect our client and recruited expert by phone, face-to-face meetings and etc. We are a global expert network firm that is focused on delivering high-quality experts to our clients throughout the world. Our clients include multinational corporations, global consulting firms, private equity firms, venture capital firms, asset management companies.
We have made new logo and please find attachment.(Please use new logo)
Target Market(s)
Global Consulting Firms, Investment Firms, Private Equity Firms, Venture Capital Firms.
Industry/Entity Type
Recruitment
Contact Information for Business Card
We need two Languages (English and Korean Version).
The front is Korean and the back is English version.
[The back] [English]
Company Name: Corwell Insight Partners, Inc.
CEO Name: Daniel Park
Address: #507, Hanbit Bldg, 82 Maebongsan-ro, Dobong-gu, Seoul, 01327, Korea
Tel. +82 2 718 4052
Fax. +82 2 864 1097
Mobile. +82 10 7264 8815
Email: daniel@corwellip.com
Web: www.corwellip.com
[The front] [Korean] => Described in same order as English version.
회사명: 코웰인사이트파트너스(주)
대표이사: 박도현
주소: 서울시 도봉구 매봉산로 82 한빛빌딩 507호
Tel. 02 718 4052
Fax. 02 864 1097
Mobile. 010 7264 8815
Web: www.corwellip.com
Look and feel
Each slider illustrates characteristics of the customer's brand and the style your logo design should communicate.

```html
<!DOCTYPE html>
<html lang="ko">
<head>
<meta charset="utf-8">
<title>Corwell Insight Partners – Business Card (Korean side)</title>
<link rel="stylesheet" href="https://fonts.googleapis.com/css2?family=Marcellus&family=Open+Sans:wght@400&family=Noto+Sans+KR:wght@400&display=swap">
<style>
  :root {
    --navy: #1c2452;
    --white: #ffffff;
    --accent-red: #d8452a;
    --accent-orange: #ef5a24;
    --accent-brown: #7a300d;
  }
  html, body {
    margin: 0;
    padding: 0;
    width: 1200px;
    height: 667px;
    overflow: hidden;
    background: var(--navy);
  }
  .card {
    position: relative;
    width: 1200px;
    height: 667px;
    background: var(--navy);
    overflow: hidden;
  }
  .corner-accent {
    position: absolute;
    top: 0;
    left: 0;
    width: 1200px;
    height: 667px;
  }
  .brand-name {
    position: absolute;
    left: 161px;
    top: 182px;
    margin: 0;
    font-family: "Marcellus", "Times New Roman", serif;
    font-weight: 400;
    font-size: 66px;
    line-height: 100px;
    letter-spacing: 0;
    color: var(--white);
    text-transform: uppercase;
  }
  .brand-name span { display: block; }
  .contact-divider {
    position: absolute;
    left: 584px;
    top: 403px;
    width: 4px;
    height: 264px;
    background: var(--white);
  }
  .contact-list {
    position: absolute;
    left: 610px;
    top: 404px;
    margin: 0;
    padding: 0;
    list-style: none;
    font-family: "Open Sans", "Noto Sans KR", sans-serif;
    font-size: 20px;
    line-height: 28.3px;
    color: var(--white);
    white-space: nowrap;
  }
  .contact-list .ko {
    font-family: "Noto Sans KR", "Open Sans", sans-serif;
    font-weight: 400;
    font-size: 21px;
  }
</style>
</head>
<body>
  <div class="card">
    <svg class="corner-accent" viewBox="0 0 1200 667" role="img" aria-label="Warm orange-to-rust angular accent in the top right corner">
      <defs>
        <linearGradient id="accent-fade" x1="0" y1="0" x2="1" y2="1">
          <stop offset="0" stop-color="var(--accent-red)"/>
          <stop offset="0.45" stop-color="var(--accent-orange)"/>
          <stop offset="1" stop-color="var(--accent-brown)"/>
        </linearGradient>
      </defs>
      <polygon points="600,0 1200,0 1200,488" fill="url(#accent-fade)"/>
    </svg>

    <h1 class="brand-name">
      <span>Corwell</span>
      <span>Insight</span>
      <span>Partners</span>
    </h1>

    <div class="contact-divider"></div>

    <ul class="contact-list">
      <li class="ko">회사명: 코웰인사이트파트너스(주)</li>
      <li class="ko">대표이사: 박도현</li>
      <li class="ko">주소: 서울시 도봉구 매봉산로 82 한빛빌딩 507호</li>
      <li>Tel. 02 718 4052</li>
      <li>Fax. 02 864 1097</li>
      <li>Mobile. 010 7264 8815</li>
      <li>Email: daniel@corwellip.com</li>
      <li>Web: www.corwellip.com</li>
    </ul>
  </div>
</body>
</html>
```